Postcard design- Promoting Conveyancing services to Property Developers

We require a double sided postcard design with the following measurements:

148mm x 210mm
Leaving space for address and stamp on the back
(Printer requirements: 3mm internal bleed on each document and 3mm external bleed on each document. Digital file supplied as a press ready PDF. Full colour CMYK and please include trim marks

On the front the following large text (and any of your graphics):

'We lodge plans of subdivision'

I NOTE THAT THE WORDS SHOULD BE THE FOCUS POINT AND THE GRAPHICS SHOULD NOT BE TOO DOMINATING.

On the back:

Address panel and stamp section to the right and then the following text to the left:

Harwicks- Lindell Bay Conveyancing (see our logo on website and as attached)

We are the developer experts.

Until ............... (LEAVE DATE BLANK) we will be lodging plans of subdivision including:

IN SMALL PRINT:

Preparation of Land Titles Office Form 10 (Plan of Subdivision or Consolidation) and Limited/Unlimited Owners Corporation Information; Arrange for mortgagee consent, stamping of plan and making title available; Lodge plan at Land Titles Office; Follow up your surveyor for Statement of Compliance, Follow up Land Titles Office and notify you immediately upon registration.

PRICE SECTION:

If you do not hold a mortgage over the title our office will collect the new titles on your behalf. ...) for $330.00 (50% discount off normal price) including GST for new clients. We are prompt, friendly and fully understand property developers needs.

(THE PRICE SHOULD BE HIGHLIGHTED AND LARGER)

Harwicks- Lindell Bay
Level 4, 12 Quarry Lane, Melbourne, 3120
harwicks.com.au
Ph: 03 9412 7730
Email: mabel@harwicks.com.au

(THIS ADDRESS SECTION SHOULD BE SMALLER)

Sorry about all the attachments. You can use as many or as little as you like or even none.

Also, I don't know the exact font on our logo but we usually use ACADEMY ENGRAVED LET if we want to match it (and we don't expect the designs have to match it).

Target Market(s)

Small property developers who are needing to have documents lodged at the Land Titles Office

Industry/Entity Type

Surveyor

Requirements
Must have
• Text as above.

```html
<!DOCTYPE html>
<html lang="en">
<head>
<meta charset="utf-8">
<title>Harwicks – Plans of Subdivision Postcard</title>
<link href="https://fonts.googleapis.com/css2?family=Bebas+Neue&family=Questrial&display=swap" rel="stylesheet">
<style>
  :root {
    --page: #ffffff;
    --card-green: #8cc63f;
    --lime: #d4e021;
    --lime-soft: #c9dc3c;
    --dot-white: #f4f9ec;
    --magenta: #e6007e;
    --ink: #3a3a3a;
    --ink-soft: #555555;
    --price: #111111;
    --box-line: #9a9a9a;
    --shade: #e4e4e4;
    --brand: #1f2a5c;
  }
  * { margin: 0; padding: 0; box-sizing: border-box; }
  html, body { width: 1200px; height: 900px; overflow: hidden; background: var(--page); }
  body { position: relative; font-family: "Questrial", "Helvetica Neue", Arial, sans-serif; color: var(--ink); }

  /* Front of postcard */
  .card-front {
    position: absolute; left: 42px; top: 62px; width: 529px; height: 373px;
    background: var(--card-green); border: 1px solid #444; overflow: hidden;
  }
  .front-headline {
    position: absolute; left: 19px; top: 6px;
    font-family: "Bebas Neue", "Oswald", sans-serif; font-weight: 400;
    font-size: 53px; line-height: 1; color: var(--magenta);
    letter-spacing: -0.2px; word-spacing: -5px; white-space: nowrap;
  }
  .front-artwork {
    position: absolute; left: 58px; top: 78px; width: 471px; height: 295px;
    background:
      radial-gradient(ellipse 32% 58% at 86% 78%, var(--lime) 0%, var(--lime) 55%, rgba(212,224,33,0) 100%),
      radial-gradient(ellipse 30% 48% at 34% 76%, var(--lime-soft) 0%, rgba(201,220,60,0.85) 45%, rgba(201,220,60,0) 100%),
      radial-gradient(ellipse 78% 100% at 72% 100%, rgba(244,249,236,0.75) 0%, rgba(244,249,236,0.55) 45%, rgba(244,249,236,0.25) 75%, rgba(244,249,236,0) 100%);
  }

  /* Back of postcard */
  .card-back {
    position: absolute; left: 631px; top: 443px; width: 529px; height: 375px;
    background: var(--page); border: 1px solid #444; overflow: hidden;
  }
  .back-backdrop {
    position: absolute; left: 0; top: 280px; width: 320px; height: 95px;
    background: linear-gradient(180deg, rgba(228,228,228,0) 0%, var(--shade) 65%, #dcdcdc 100%);
  }
  .brand {
    position: absolute; left: 16px; top: 10px; display: flex; align-items: center; gap: 8px;
    font-size: 26px; color: var(--brand); line-height: 1;
  }
  .brand-square { width: 14px; height: 14px; background: var(--brand); }
  .intro { position: absolute; left: 14px; top: 55px; font-size: 9.5px; }
  .until { position: absolute; left: 16px; top: 77px; font-size: 9.5px; }
  .services {
    position: absolute; left: 12px; top: 99px; width: 330px;
    font-size: 7.6px; line-height: 10.3px; list-style: none;
  }
  .offer {
    position: absolute; left: 9px; top: 186px; width: 290px;
    font-size: 12px; line-height: 15.4px;
  }
  .offer-price {
    display: inline-block; font-size: 15px; line-height: 17px;
    font-weight: 700; color: var(--price); -webkit-text-stroke: 0.5px var(--price);
  }
  .contact {
    position: absolute; left: 8px; top: 315px; font-style: normal;
    font-size: 8px; line-height: 10.5px; color: var(--ink-soft);
  }
  .stamp-box {
    position: absolute; left: 469px; top: 7px; width: 54px; height: 71px; border: 1px solid var(--box-line);
  }
  .address-line {
    position: absolute; left: 292px; width: 230px; height: 23px;
    border: 1px solid var(--box-line); background: var(--page);
  }
  .address-line.l1 { top: 253px; }
  .address-line.l2 { top: 283px; }
  .address-line.l3 { top: 313px; }
  .address-line.l4 { top: 341px; }
</style>
</head>
<body>

<section class="card-front">
  <h1 class="front-headline">WE LODGE PLANS OF SUBDIVISION</h1>
  <div class="front-artwork" role="img" aria-label="Illustration of a fanned white dot pattern with a lime tree and a lime apartment building"></div>
</section>

<section class="card-back">
  <div class="back-backdrop" role="img" aria-label="Faint grey photo of a street tree and building"></div>

  <div class="brand"><span class="brand-square"></span><span class="brand-name">Harwicks</span></div>

  <p class="intro">We are the developer experts.</p>
  <p class="until">Until ............... &nbsp;we will be lodging plans of subdivision including:</p>

  <ul class="services">
    <li>Preparation of Land Titles Office Form 10 (Plan of Subdivision or Consolidation)</li>
    <li>and Limited/Unlimited Owners Corporation Information;</li>
    <li>Arrange for mortgagee consent,</li>
    <li>stamping of plan and making title available;</li>
    <li>Lodge plan at Land Titles Office;</li>
    <li>Follow up your surveyor for Statement of Compliance,</li>
    <li>Follow up Land Titles Office and notify you immediately upon registration.</li>
  </ul>

  <p class="offer">
    If you do not hold a mortgage over the title<br>
    our office will collect the new titles on your behalf<br>
    <span class="offer-price">for $330.00</span><br>
    (50% discount off normal price) including GST<br>
    for new clients. &nbsp;We are prompt, friendly and fully<br>
    understand property developers needs.
  </p>

  <address class="contact">
    Harwicks- Lindell Bay<br>
    Level 4, 12 Quarry Lane, Melbourne, 3120<br>
    harwicks.com.au<br>
    Ph: 03 9412 7730<br>
    Email: mabel@harwicks.com.au
  </address>

  <div class="stamp-box"></div>
  <div class="address-line l1"></div>
  <div class="address-line l2"></div>
  <div class="address-line l3"></div>
  <div class="address-line l4"></div>
</section>

</body>
</html>
```